A layout of a webpage for oil trade platform

I would like to have a desgin of one page webpage (with section scrollling dowin) that woulf present the new product i.e. oil trade platform for wholesale buyers and sellers.
Layout should consist of the sections similar to the given at: https://klinika.pewnywybor.pl/system-zarzadzania-wizytami
However oil industy require more colors and more photo stories than here for doctor.
I. I woul imagine at first below menu a slider with brueg information about the product and its advantages with "more" button next to the prict screen of our platform on different displays (PC and mobile).
II. Bellow the slider I would imagine icons correspoing to the advantages of that plaftorm:
1. Purchase/sale process automation 24/7
2. Access to the best deals
3. Electronic offerings and orderings
4. Transaction status monitoring
5. Data and transaction security
II A) (optional):
In near future we would like to prepare a short video presenation. Hence please prepare a place to display that element here.
At the moment alternatvily please prepare a How it works section that would explan the platform operating process
III. Next secion is about benefits for Oil Purchaser
It can be done either by icons of by text and corresponding grahip for while section.
Benefits:
- Access to cheaper oil
- Convenience of online orders
- Possibility to compare prices on the market
- Transaction history
- Order status monitoring
- Seccurity and transparency of purchase
IV. Next seciont is about benefits for Oil Seller
Benefits:
- New sale channel
- Attracting new clients
- More oil sold
- Transaction security
- Possibility to integrate with distribution infrastructure and logistits for more efficient automation.
V. Contact form
VI. Footer
I would need a layout that that will correspond to the very dynamic logo but I would expect also a clean form, smoth and modern. It has to be proffessional layout with more corporate character.
It can use a paralax features if needed.

```html
<!DOCTYPE html>
<html lang="en">
<head>
<meta charset="utf-8">
<title>Crudeline – Oil Trade Platform</title>
<link href="https://fonts.googleapis.com/css2?family=Roboto:wght@300;400;500;700&family=Kaushan+Script&display=swap" rel="stylesheet">
<style>
:root{
  --navy:#0f2347;
  --navy-deep:#0a1a38;
  --orange:#f58634;
  --orange-strong:#f26a2a;
  --text:#3a3f4a;
  --muted:#8a8f99;
  --line:#e6e8ec;
  --light:#f6f7f9;
  --footer:#2b2826;
  --footer-bar:#1f1d1c;
}
*{margin:0;padding:0;box-sizing:border-box}
html,body{width:727px;height:1200px;overflow:hidden}
body{font-family:'Roboto',sans-serif;color:var(--text);background:#fff;position:relative}

/* header */
.site-header{position:absolute;left:0;top:0;width:727px;height:32px;background:#fff}
.brand{position:absolute;left:106px;top:9px;display:flex;align-items:center;gap:5px;font-weight:700;font-size:10px;color:var(--navy);letter-spacing:.2px}
.brand-dot{width:10px;height:10px;border-radius:50%;background:var(--orange)}
.main-nav{position:absolute;right:111px;top:11px;display:flex;font-size:8px;color:var(--muted)}
.main-nav a{color:inherit;text-decoration:none;padding:0 6px;border-left:1px solid #cfd3d9;line-height:9px}
.main-nav a:first-child{border-left:0;color:#1c2230;font-weight:700}

/* hero */
.hero{position:absolute;left:0;top:32px;width:727px;height:272px;background:linear-gradient(100deg,#0c1f42 0%,#12295a 60%,#163063 100%);overflow:hidden}
.hero-visual{position:absolute;left:323px;top:0;width:404px;height:272px;background:radial-gradient(ellipse at 55% 45%,#2a3a55 0%,#1a2d52 45%,transparent 75%),linear-gradient(90deg,transparent,#1b2f57 30%,#142a55)}
.hero-title{position:absolute;left:106px;top:71px;font-weight:300;font-size:23px;line-height:23px;color:#fff;letter-spacing:.3px}
.hero-text{position:absolute;left:106px;top:124px;width:225px;font-size:8.2px;line-height:12px;color:#c8d1e2;font-weight:300}
.btn-outline{position:absolute;left:104px;top:173px;width:88px;height:24px;border:1px solid #fff;color:#fff;font-size:7.5px;display:flex;align-items:center;justify-content:center;letter-spacing:.3px}
.scroll-mouse{position:absolute;left:355px;top:227px;width:17px;height:28px;border:1.5px solid #fff;border-radius:9px}
.scroll-mouse::after{content:"";position:absolute;left:6px;top:5px;width:2px;height:5px;background:#fff;border-radius:1px}
.slider-dots{position:absolute;left:490px;top:243px;display:flex;gap:3px}
.slider-dots span{width:5px;height:5px;border-radius:50%;background:#fff}
.slider-dots span:first-child{background:var(--orange)}

/* features */
.features{position:absolute;left:0;top:304px;width:727px;height:64px;background:#fff;display:flex;padding-left:104px}
.feature{width:104px;height:64px;border-right:1px solid var(--line);display:flex;flex-direction:column;align-items:center;padding-top:11px;font-size:6.3px;line-height:7.5px;color:var(--muted);text-align:center}
.feature:last-child{border-right:0}
.feature svg{width:20px;height:20px;margin-bottom:5px}
.feature.is-active{background:var(--orange);color:#fff}

/* purchaser */
.purchaser{position:absolute;left:0;top:368px;width:727px;height:278px;background:#fff}
.purchaser-photo{position:absolute;left:0;top:0;width:364px;height:278px;background:linear-gradient(135deg,#e9edf2 0%,#cfd8e3 45%,#b9c6d6 70%,#dfe5ec 100%)}
.section-title{font-size:13px;font-weight:300;color:#1c2230}
.section-title b{font-weight:500}
.purchaser .section-title{position:absolute;left:403px;top:41px}
.benefit-list{list-style:none;position:absolute}
.benefit-list li{display:flex;align-items:center;font-size:8px;font-weight:300}
.benefit-list svg{width:14px;height:14px;margin-right:15px;flex:none}
.purchaser .benefit-list{left:405px;top:73px}
.purchaser .benefit-list li{height:27.4px;color:#3a3f4a}
.video-badge{position:absolute;left:571px;top:636px;width:22px;height:22px;border-radius:50%;background:#e63a2e;display:flex;align-items:center;justify-content:center;z-index:2}

/* seller */
.seller{position:absolute;left:0;top:646px;width:727px;height:273px;background:linear-gradient(180deg,#f58a3a,#f3832f)}
.seller .section-title{position:absolute;left:151px;top:64px;color:#fff}
.seller .benefit-list{left:151px;top:90px;color:#fff}
.seller .benefit-list li{height:28px}
.seller .benefit-list li.multi{height:auto;align-items:flex-start;margin-top:3px;line-height:9.6px}
.seller .benefit-list svg{margin-right:14px}
.phone-visual{position:absolute;left:402px;top:54px;width:146px;height:219px;border-radius:22px 22px 0 0;background:linear-gradient(180deg,#f3f4f6,#e3e6ea)}

/* contact */
.contact{position:absolute;left:0;top:919px;width:727px;height:154px;background:var(--light)}
.contact .section-title{position:absolute;left:0;width:727px;top:22px;text-align:center;font-size:14px;font-weight:400}
.contact-lead{position:absolute;left:130px;top:48px;width:467px;text-align:center;font-size:6.2px;line-height:10px;color:var(--muted)}
.field{position:absolute;background:#fff;border:1px solid #eceef1;font-size:6.5px;color:var(--muted);display:flex;align-items:center;padding-left:6px;gap:5px}
.field-msg{align-items:flex-start;padding-top:5px}
.btn-send{position:absolute;left:480px;top:80px;width:59px;height:39px;background:var(--orange-strong);color:#fff;font-size:13px;display:flex;align-items:center;justify-content:center}

/* footer */
.site-footer{position:absolute;left:0;top:1073px;width:727px;height:105px;background:linear-gradient(180deg,#35302c,#26231f);border-top:2px solid var(--orange-strong)}
.foot-col{position:absolute;top:18px;font-size:6.2px;line-height:11px;color:#b7b1aa}
.foot-col h4{font-size:7.5px;color:#fff;font-weight:500;margin-bottom:3px;line-height:9px}
.foot-col.nohead{top:30px}
.contact-line{display:flex;gap:5px}
.contact-line svg{flex:none;margin-top:2px}
.phone-line{font-size:8px;color:#fff}
.footer-bar{position:absolute;left:0;top:1178px;width:727px;height:22px;background:var(--footer-bar)}
.copyright{position:absolute;left:105px;top:8px;font-size:5.5px;color:#8e8882}
.follow{position:absolute;left:509px;top:5px;font-family:'Kaushan Script',cursive;font-size:7.5px;color:#fff}
.social{position:absolute;left:566px;top:5px;display:flex;gap:2px}
.social span{width:12px;height:12px}
</style>
</head>
<body>

<header class="site-header">
  <div class="brand"><span class="brand-dot"></span>CRUDELINE</div>
  <nav class="main-nav">
    <a>Home</a><a>Company</a><a>Energy News</a><a>Projects</a><a>Contact Us</a>
  </nav>
</header>

<section class="hero">
  <div class="hero-visual" role="img" aria-label="Hands holding a tablet showing the trading platform dashboard"></div>
  <h1 class="hero-title">TRANSPORTING<br>OIL &amp; NATURAL GAS</h1>
  <p class="hero-text">Advances in exploration and production have helped to locate and recover a supply of oil and natural gas from major reserves across the globe.</p>
  <a class="btn-outline">LEARN MORE</a>
  <div class="scroll-mouse"></div>
  <div class="slider-dots"><span></span><span></span><span></span></div>
</section>

<section class="features">
  <div class="feature">
    <svg viewBox="0 0 24 24" fill="none" stroke="#f58634" stroke-width="1.3"><circle cx="12" cy="12" r="6"/><path d="M4 10a8 8 0 0 1 14-5M20 14a8 8 0 0 1-14 5M18 2v3h-3M6 22v-3h3"/><path d="M12 9v6M10 10.5h3a1 1 0 0 1 0 2h-2a1 1 0 0 0 0 2h3"/></svg>
    Purchase/sale process<br>automation 24/7
  </div>
  <div class="feature">
    <svg viewBox="0 0 24 24" fill="none" stroke="#f58634" stroke-width="1.3"><path d="M2 11l5-5 4 3 4-3 7 5-8 7-3-2-3-2z"/><path d="M9 13l3 3M11 11l3 3"/></svg>
    Access to<br>the best deals
  </div>
  <div class="feature is-active">
    <svg viewBox="0 0 24 24" fill="none" stroke="#fff" stroke-width="1.3"><circle cx="12" cy="12" r="9"/><path d="M9 15l6-6"/><circle cx="9.5" cy="9.5" r="1"/><circle cx="14.5" cy="14.5" r="1"/></svg>
    Electronic offerings<br>and orderings
  </div>
  <div class="feature">
    <svg viewBox="0 0 24 24" fill="none" stroke="#f58634" stroke-width="1.3"><rect x="3" y="4" width="18" height="12" rx="1"/><path d="M9 20h6M12 16v4M8 11l3-3 2 2 3-3"/></svg>
    Transaction status<br>monitoring
  </div>
  <div class="feature">
    <svg viewBox="0 0 24 24" fill="none" stroke="#f58634" stroke-width="1.3"><ellipse cx="12" cy="5" rx="7" ry="2.5"/><path d="M5 5v14c0 1.4 3 2.5 7 2.5s7-1.1 7-2.5V5M5 10c0 1.4 3 2.5 7 2.5s7-1.1 7-2.5"/><rect x="10" y="14" width="4" height="3"/></svg>
    Data and transaction<br>security
  </div>
</section>

<section class="purchaser">
  <div class="purchaser-photo" role="img" aria-label="Hands using a tablet with colourful bar and pie charts on an office desk"></div>
  <h2 class="section-title">Oil Purchaser <b>Benefits</b></h2>
  <ul class="benefit-list">
    <li><svg viewBox="0 0 16 16" fill="none" stroke="#3a3f4a" stroke-width="1"><circle cx="5" cy="5" r="3.5"/><path d="M7.5 7.5l6 6M11 11l-1.5 1.5M13 13l-1.5 1.5"/></svg>Access to cheaper oil</li>
    <li><svg viewBox="0 0 16 16" fill="none" stroke="#3a3f4a" stroke-width="1"><path d="M1 2h2l2 8h8l1.5-6H4"/><circle cx="6" cy="13" r="1"/><circle cx="12" cy="13" r="1"/></svg>Convenience of online orders</li>
    <li><svg viewBox="0 0 16 16" fill="#3a3f4a"><rect x="1" y="10" width="2" height="5"/><rect x="4" y="8" width="2" height="7"/><rect x="7" y="9" width="2" height="6"/><rect x="10" y="5" width="2" height="10"/><rect x="13" y="2" width="2" height="13"/></svg>Possibility to compare prices on the market</li>
    <li><svg viewBox="0 0 16 16" fill="none" stroke="#3a3f4a" stroke-width="1"><path d="M2.5 5A6.5 6.5 0 1 1 1.5 8"/><path d="M1 2v3.5h3.5M8 4.5V8l2.5 2"/></svg>Transaction history</li>
    <li><svg viewBox="0 0 16 16" fill="none" stroke="#3a3f4a" stroke-width="1"><path d="M1 3h9v8H1zM10 6h3l2 3v2h-5"/><circle cx="4" cy="12.5" r="1.3"/><circle cx="12" cy="12.5" r="1.3"/><path d="M3.5 7l1.5 1.5 3-3"/></svg>Order status monitoring</li>
    <li><svg viewBox="0 0 16 16" fill="#3a3f4a"><circle cx="2" cy="2" r="1.4"/><circle cx="6" cy="2" r="1.4"/><circle cx="10" cy="2" r="1"/><circle cx="2" cy="6" r="1.4"/><circle cx="6" cy="6" r="1.4"/><circle cx="10" cy="6" r="1"/><circle cx="14" cy="6" r="0.8"/><circle cx="2" cy="10" r="1.4"/><circle cx="6" cy="10" r="1"/><circle cx="10" cy="10" r="1"/><circle cx="2" cy="14" r="1.4"/><circle cx="6" cy="14" r="1"/><circle cx="10" cy="14" r="0.8"/></svg>Seccurity and transparency of purchase</li>
  </ul>
</section>

<div class="video-badge"><svg width="12" height="10" viewBox="0 0 12 10" fill="none" stroke="#fff" stroke-width="1"><rect x=".5" y=".5" width="11" height="9" rx="2"/><path d="M4.5 3v4l3-2z" fill="#fff"/></svg></div>

<section class="seller">
  <h2 class="section-title">Oil Seller <b>Benefits</b></h2>
  <ul class="benefit-list">
    <li><svg viewBox="0 0 16 16" fill="none" stroke="#fff" stroke-width="1"><path d="M8 1l6 6-7 7-6-6V2z"/><circle cx="5" cy="5" r="1"/><path d="M6 10l4-4"/></svg>New sale channel</li>
    <li><svg viewBox="0 0 16 16" fill="#fff"><circle cx="8" cy="5" r="2"/><path d="M5 11a3 3 0 0 1 6 0z"/><circle cx="2.5" cy="8" r="1.3"/><circle cx="13.5" cy="8" r="1.3"/><circle cx="4" cy="2.5" r="1"/><circle cx="12" cy="2.5" r="1"/><circle cx="4" cy="13.5" r="1"/><circle cx="12" cy="13.5" r="1"/></svg>Attracting new clients</li>
    <li><svg viewBox="0 0 16 16" fill="none" stroke="#fff" stroke-width="1"><path d="M1 1v14h14M3 12l4-4 3 2 5-6"/><path d="M11 12c0-1.5 1.5-3 1.5-3s1.5 1.5 1.5 3a1.5 1.5 0 0 1-3 0z"/></svg>More oil sold</li>
    <li><svg viewBox="0 0 16 16" fill="none" stroke="#fff" stroke-width="1"><rect x="1" y="5" width="11" height="9"/><path d="M4 5V1h11v10h-3"/><path d="M6.5 7.5v5M8 8.5H6a1 1 0 0 0 0 2h1a1 1 0 0 1 0 2H5"/></svg>Transaction security</li>
    <li class="multi"><svg viewBox="0 0 16 16" fill="none" stroke="#fff" stroke-width="1"><circle cx="3" cy="3" r="2"/><circle cx="8" cy="3" r="2"/><circle cx="13" cy="3" r="2"/><path d="M1 15V7h4v8M6 15V7h4v8M11 15V7h4v8M1 11h14"/></svg>Possibility to integrate with distribution<br>infrastructure and logistits for more<br>efficient automation</li>
  </ul>
  <div class="phone-visual" role="img" aria-label="Smartphone showing the sales summary screen with a blue bar chart"></div>
</section>

<section class="contact">
  <h2 class="section-title">Contact Us</h2>
  <p class="contact-lead">This is the studio's version of Lorem Ipsum. Proin gravida nibh vel velit auctor aliquet. Aenean sollicitudin, lorem quis bibendum auctor, nisi elit consequat ipsum, nec sagittis sem nibh id elit. Duis sed odio sit amet nibh vulputate cursus a sit amet mauris. Morbi accumsan ipsum velit.</p>
  <div class="field" style="left:188px;top:80px;width:142px;height:19px"><svg width="7" height="7" viewBox="0 0 8 8" fill="#c3c7cd"><circle cx="4" cy="2.2" r="2"/><path d="M0 8a4 3.5 0 0 1 8 0z"/></svg>Name</div>
  <div class="field" style="left:188px;top:100px;width:142px;height:19px"><svg width="8" height="6" viewBox="0 0 8 6" fill="none" stroke="#c3c7cd"><rect x=".5" y=".5" width="7" height="5"/><path d="M.5 .5l3.5 3 3.5-3"/></svg>Email</div>
  <div class="field field-msg" style="left:335px;top:80px;width:141px;height:39px">Message</div>
  <a class="btn-send">Send</a>
</section>

<footer class="site-footer">
  <div class="foot-col" style="left:105px"><h4>Life in Oil &amp; Gas</h4>Oil and Gas Journey<br>Oil and Gas Guide<br>Life Onshore<br>Life Offshore<br>Training<br>Safety</div>
  <div class="foot-col nohead" style="left:178px">Case Studies<br>Petroleum Study Hub Online</div>
  <div class="foot-col" style="left:268px"><h4>Careers</h4>Oil &amp; Gas Industry Roles<br>Career Planner<br>Find a job<br>Oil and Gas Company Careers Websites<br>Oil and Gas Technica<br>Skills Matrix</div>
  <div class="foot-col" style="left:412px"><h4>Events</h4>Power Up Your Future<br>Industry Awareness Events<br>Energy Career Planner App<br>Resources<br>Industry Insight Week<br>Careers Opportunity Week</div>
  <div class="foot-col" style="left:545px;line-height:8px"><h4>Contact</h4>
    <div class="contact-line"><svg width="6" height="8" viewBox="0 0 6 8" fill="#b7b1aa"><path d="M3 0a3 3 0 0 1 3 3c0 2-3 5-3 5S0 5 0 3a3 3 0 0 1 3-3z"/></svg><span>Crudeline<br>418 W. Harbor Ave.<br>STE 310 - 12<br>Tulsa, OK 74103</span></div>
    <div class="contact-line" style="margin-top:5px;align-items:center"><svg width="8" height="6" viewBox="0 0 8 6" fill="#b7b1aa"><rect width="8" height="6" rx="1"/></svg><span class="phone-line">(555) 204-7190</span></div>
    <div class="contact-line" style="margin-top:2px;align-items:center"><svg width="8" height="6" viewBox="0 0 8 6" fill="none" stroke="#b7b1aa"><rect x=".5" y=".5" width="7" height="5"/><path d="M.5 .5l3.5 3 3.5-3"/></svg><span>sales@crudeline.com</span></div>
  </div>
</footer>
<div class="footer-bar">
  <span class="copyright">© 2017 Crudeline. All Rights Reserved.</span>
  <span class="follow">Follow Us On</span>
  <div class="social"><span style="background:#3b5a9a"></span><span style="background:#2aa3dc"></span><span style="background:#1a78b4"></span><span style="background:#d8432f"></span></div>
</div>

</body>
</html>
```